Young judge needs a website to publish and to connect

I would like to have a website where I can publish my articles in public law. I am judge at the Alpine Civic Appeals Chamber. Therefore, the website must have a calm, friendly and fairly neutral design. Also, it should be mobile friendly and easy to use.

On my website, I want to

- publish articles such as https://www.quorvely.com/notes/how-win-court-tobias-wrenholt/ and get feedbacks from my colleagues
- generate interest for my project on 'Rules and Ballots - Notes from the Dais', a book that I would like to publish in 2020 and which brings together my publications on public law (http://www.statutewell.ch/content/english/profil/publikationen.html ).
- provide updates for my university courses on constitutional, administrative and international law.

For that purpose, I would kindly ask you to suggest a website that communicates a fresh approach to the work of a young judge in constitutional and administrative law. Please have in mind that I do not only sit on the bench, but that I also work in academia. Therefore, it should be suitable for an audience from both university and law practice. The website should replace the existing website on www.statutewell.ch that I designed when still working as a lawyer. Thank you.

Target Market(s)

Academica, law firms, courts

Industry/Entity Type

University

Contact Information for Business Card

Tobias Wrenholt
Judge
Alpine Civic Appeals Chamber
M +41 78 5XX 9X 2X

Logo Text

Notes from the Dais

Number of Pages Required

5+ page

Font styles to use
Sans Serif

Colors
0455a3

Requirements
Must have
• - a page where I can publish and get feedbacks
• - a page about my project on law and politics
• - a page where I can provide updates for my university courses on constitutional, administrative and international law
• - page where I can list current and planned projects
• - a collaborative, young and fresh approach
Nice to have
• - a page reserved for my colleagues at the Alpine Civic Appeals Chamber where I can alert them about to possibility to collaborate (if possibly password protected) and where they may suggest what to contribute to a specific project
Should not have
• anything which might to suggest that I want to make money with it, bragging or pretentious. Do not forget: I am judge, not a barrister.

```html
<!DOCTYPE html>
<html lang="en">
<head>
<meta charset="utf-8">
<title>Tobias Wrenholt – Latest Articles</title>
<link href="https://fonts.googleapis.com/css2?family=Cormorant+Garamond:ital,wght@0,400;0,500;0,600;1,400&display=swap" rel="stylesheet">
<style>
  :root {
    --ink: #1b1b1b;
    --text: #2a2a2a;
    --muted: #b9b9b9;
    --rule: #8c8c8c;
    --accent: #0455a3;
    --white: #ffffff;
    --nav-active: #111111;
    --footer-band: #e6e6e6;
  }
  * { box-sizing: border-box; margin: 0; padding: 0; }
  html, body { width: 1200px; height: 2908px; overflow: hidden; }
  body {
    position: relative;
    background: var(--white);
    color: var(--text);
    font-family: "Cormorant Garamond", Georgia, serif;
  }
  .abs { position: absolute; }

  /* Header */
  .site-header { left: 0; top: 0; width: 1200px; height: 60px; background: var(--white); }
  .brand { left: 84px; top: 14px; font-size: 17px; font-weight: 600; letter-spacing: 0.5px; color: var(--ink); line-height: 1; }
  .brand-sub { display: block; font-size: 9px; letter-spacing: 1.6px; text-transform: uppercase; margin-top: 6px; }
  .main-nav { left: 642px; top: 0; height: 60px; display: flex; }
  .main-nav a { display: block; height: 60px; line-height: 64px; font-size: 14.5px; font-weight: 600; color: var(--ink); text-decoration: none; }
  .main-nav .nav-home { width: 82px; text-align: center; background: var(--nav-active); color: var(--white); margin-right: 60px; }
  .main-nav .nav-articles { margin-right: 24px; }
  .main-nav .nav-courses { margin-right: 34px; }
  .main-nav .nav-projects { margin-right: 32px; }

  /* Hero */
  .hero { left: 0; top: 60px; width: 1200px; height: 336px;
    background: linear-gradient(90deg, #6d6f70 0%, #7a7f84 30%, #6f747b 60%, #5d636b 100%); }
  .hero-title { left: 0; top: 200px; width: 1200px; text-align: center; font-size: 56px; font-weight: 500; color: var(--white); text-shadow: 0 3px 8px rgba(0,0,0,0.55); }
  .hero-edge { left: 0; top: 396px; width: 1200px; height: 8px; background: #d9dbde; }

  /* Sidebar */
  .section-heading { font-size: 20px; font-weight: 500; color: var(--ink); padding-bottom: 4px; border-bottom: 1.5px solid var(--rule); }
  .sidebar-list { left: 82px; width: 469px; }
  .teaser { display: flex; height: 125px; margin-top: 21px; }
  .teaser-thumb { width: 190px; height: 125px; flex: none; }
  .teaser-text { margin-left: 15px; font-size: 15.5px; line-height: 25px; color: var(--text); margin-top: -4px; }
  .read-more { color: var(--accent); text-decoration: underline; font-weight: 600; margin-left: 8px; }

  .thumb-suits { background: linear-gradient(90deg, #3a3e45, #8a8f96, #2f333a); }
  .thumb-desk { background: linear-gradient(135deg, #7a5434, #b98c5e 55%, #4a3220); }
  .thumb-meeting { background: linear-gradient(90deg, #3d4652, #c5ccd5 55%, #5a4a3a); }
  .thumb-scales { background: linear-gradient(135deg, #5a3320, #a6703f 50%, #3d2518); }
  .thumb-library { background: linear-gradient(135deg, #6a4a2d, #c99a63 50%, #7a2e2e); }
  .thumb-books { background: linear-gradient(135deg, #f2f2f2, #6b4a35 60%, #f4f4f4); }

  /* Course updates */
  .course-card { left: 82px; top: 1696px; width: 465px; height: 459px;
    background: linear-gradient(90deg, #585d62 0%, #6c7176 55%, #5e5a55 78%, #c9ccce 80%, #e9eaeb 100%); }
  .course-content { left: 114px; top: 1722px; width: 330px; color: #f1f1f1; }
  .course-title { font-size: 31px; font-weight: 500; color: var(--white); padding-bottom: 8px; border-bottom: 2px solid #e6e6e6; }
  .course-text { margin-top: 14px; font-size: 15px; line-height: 19px; }
  .course-text .read-more { color: var(--white); }
  .slider-arrows { left: 132px; top: 2095px; display: flex; gap: 8px; }
  .slider-arrows span { width: 22px; height: 20px; display: flex; align-items: center; justify-content: center; background: rgba(40,40,40,0.55); }

  /* Article */
  .article { left: 600px; top: 448px; width: 518px; }
  .article-title { font-size: 31px; font-weight: 500; color: var(--ink); line-height: 1.2; }
  .article-date { font-size: 13px; font-style: italic; color: var(--muted); margin-top: 2px; }
  .article-photo { width: 518px; height: 407px; margin-top: 15px;
    background: linear-gradient(135deg, #1d2d4d 0%, #33466a 35%, #dfe6ef 60%, #2a3a5c 85%, #f3f5f8 100%); }
  .article-body p { font-size: 15.5px; line-height: 22.5px; margin-top: 18px; color: var(--text); }
  .article-body p:first-child { margin-top: 18px; }
  .article-photo.second { margin-top: 22px; }

  /* Author */
  .author-heading { left: 600px; top: 1988px; width: 518px; font-size: 31px; }
  .author-photo { left: 601px; top: 2060px; width: 175px; height: 175px; border-radius: 50%;
    background: radial-gradient(circle at 50% 40%, #c9a48d 0 22%, #7d8187 23% 60%, #23324a 61%); }
  .author-info { left: 823px; top: 2066px; width: 264px; }
  .author-name { font-size: 21px; font-weight: 500; color: var(--ink); }
  .author-role { font-size: 12px; font-style: italic; color: var(--muted); margin-top: -2px; }
  .small-text { font-size: 10.5px; line-height: 13.5px; color: var(--text); margin-top: 6px; }
  .social-row { display: flex; gap: 9px; margin-top: 13px; }
  .social-row span { width: 8px; height: 8px; border-radius: 50%; background: #cfcfcf; }

  /* Comments */
  .comments-heading { left: 600px; top: 2308px; width: 518px; font-size: 20px; }
  .avatar { border-radius: 50%; }
  .avatar-one { left: 605px; top: 2371px; width: 128px; height: 128px;
    background: radial-gradient(circle at 50% 45%, #e2b79a 0 28%, #a06a44 29% 45%, #f0f0f0 46%); }
  .avatar-two { left: 718px; top: 2547px; width: 132px; height: 132px;
    background: radial-gradient(circle at 50% 42%, #c9a48d 0 24%, #7d8187 25% 58%, #23324a 59%); }
  .comment { width: 250px; }
  .comment-one { left: 768px; top: 2364px; }
  .comment-two { left: 883px; top: 2546px; width: 240px; }
  .comment-head { display: flex; align-items: baseline; gap: 22px; }
  .comment-name { font-size: 20px; font-weight: 600; color: var(--accent); }
  .comment-date { font-size: 11px; color: var(--muted); }
  .reply { display: flex; align-items: center; gap: 5px; font-size: 12px; color: var(--accent); margin-top: 3px; }

  .login-row { left: 600px; top: 2732px; width: 518px; height: 46px; border-bottom: 1.5px solid var(--rule); }
  .login-label { position: absolute; left: 0; top: 10px; font-size: 20px; color: var(--ink); }
  .login-button { position: absolute; right: 0; top: 0; width: 101px; height: 36px; border: 2px solid var(--ink); background: var(--white); font-family: inherit; font-size: 17px; font-weight: 600; color: var(--ink); }

  /* Footer */
  .footer-band { left: 0; top: 2806px; width: 1200px; height: 14px; background: var(--footer-band); }
  .footer-brand { left: 84px; top: 2842px; }
  .copyright { right: 98px; top: 2852px; font-size: 13px; font-style: italic; letter-spacing: 0.4px; text-transform: uppercase; color: var(--ink); }
</style>
</head>
<body>

<header class="site-header abs">
  <div class="brand abs">Tobias Wrenholt<span class="brand-sub">Notes from the Dais</span></div>
  <nav class="main-nav abs">
    <a class="nav-home" href="#">Home</a>
    <a class="nav-articles" href="#">Articles</a>
    <a class="nav-courses" href="#">Course Updates</a>
    <a class="nav-projects" href="#">Projects</a>
    <a class="nav-contact" href="#">Contact</a>
  </nav>
</header>

<section class="hero abs" role="img" aria-label="Statue of Lady Justice holding scales against a grey sky"></section>
<h1 class="hero-title abs">Latest Articles</h1>
<div class="hero-edge abs"></div>

<aside class="sidebar-list abs" style="top:490px;">
  <h2 class="section-heading">Recent articles</h2>
  <div class="teaser">
    <div class="teaser-thumb thumb-suits" role="img" aria-label="Three colleagues in dark suits"></div>
    <p class="teaser-text">Lorem ipsum dolor sit amet, consectetur adipiscing elit. Sed id nibh leo. Vivamus tempor imperdiet auctor. Donec justo orci, scelerisque tincidunt turpis vel, pellentesque commodo ligula. <a class="read-more" href="#">Read more...</a></p>
  </div>
  <div class="teaser">
    <div class="teaser-thumb thumb-desk" role="img" aria-label="Lawyer working at a wooden desk"></div>
    <p class="teaser-text">Lorem ipsum dolor sit amet, consectetur adipiscing elit. Sed id nibh leo. Vivamus tempor imperdiet auctor. Donec justo orci, scelerisque tincidunt turpis vel, pellentesque commodo ligula. <a class="read-more" href="#">Read more...</a></p>
  </div>
  <div class="teaser">
    <div class="teaser-thumb thumb-meeting" role="img" aria-label="Colleagues talking in a conference room"></div>
    <p class="teaser-text">Lorem ipsum dolor sit amet, consectetur adipiscing elit. Sed id nibh leo. Vivamus tempor imperdiet auctor. Donec justo orci, scelerisque tincidunt turpis vel, pellentesque commodo ligula. <a class="read-more" href="#">Read more...</a></p>
  </div>
</aside>

<aside class="sidebar-list abs" style="top:1106px;">
  <h2 class="section-heading">Projects</h2>
  <div class="teaser">
    <div class="teaser-thumb thumb-scales" role="img" aria-label="Brass scales of justice on a desk"></div>
    <p class="teaser-text">Lorem ipsum dolor sit amet, consectetur adipiscing elit. Sed id nibh leo. Vivamus tempor imperdiet auctor. Donec justo orci, scelerisque tincidunt turpis vel, pellentesque commodo ligula. <a class="read-more" href="#">Read more...</a></p>
  </div>
  <div class="teaser">
    <div class="teaser-thumb thumb-library" role="img" aria-label="Man reading in a law library"></div>
    <p class="teaser-text">Lorem ipsum dolor sit amet, consectetur adipiscing elit. Sed id nibh leo. Vivamus tempor imperdiet auctor. Donec justo orci, scelerisque tincidunt turpis vel, pellentesque commodo ligula. <a class="read-more" href="#">Read more...</a></p>
  </div>
  <div class="teaser">
    <div class="teaser-thumb thumb-books" role="img" aria-label="Stack of law books with a gavel"></div>
    <p class="teaser-text">Lorem ipsum dolor sit amet, consectetur adipiscing elit. Sed id nibh leo. Vivamus tempor imperdiet auctor. Donec justo orci, scelerisque tincidunt turpis vel, pellentesque commodo ligula. <a class="read-more" href="#">Read more...</a></p>
  </div>
</aside>

<div class="course-card abs" role="img" aria-label="Globe, reading glasses and books on a study desk"></div>
<div class="course-content abs">
  <h2 class="course-title">Course updates</h2>
  <p class="course-text">Lorem ipsum dolor sit amet, consectetur adipiscing elit. Fusce ullamcorper turpis lectus, sed convallis mi porttitor eget. Duis ex risus, blandit at dui a, hendrerit tempus justo. Etiam maximus in elit non porttitor. Vestibulum venenatis at tellus vel blandit. Nulla non turpis posuere, feugiat quam rutrum, tincidunt tortor. <a class="read-more" href="#">Read more...</a></p>
</div>
<div class="slider-arrows abs">
  <span><svg width="12" height="8" viewBox="0 0 12 8"><path d="M11 4H2M5 1L2 4l3 3" stroke="#fff" stroke-width="1.4" fill="none"/></svg></span>
  <span><svg width="12" height="8" viewBox="0 0 12 8"><path d="M1 4h9M7 1l3 3-3 3" stroke="#fff" stroke-width="1.4" fill="none"/></svg></span>
</div>

<article class="article abs">
  <h2 class="article-title">Title</h2>
  <p class="article-date">June 21, 2016 at 8:15pm</p>
  <div class="article-photo" role="img" aria-label="Business people signing documents at a table"></div>
  <div class="article-body">
    <p>Lorem ipsum dolor sit amet, consectetur adipiscing elit. Sed id nibh leo. Vivamus tempor imperdiet auctor. Donec justo orci, scelerisque tincidunt turpis vel, pellentesque commodo ligula.</p>
    <p>Curabitur vehicula pharetra felis id pellentesque. Quisque tristique nisi volutpat, eleifend felis porttitor, mattis arcu. Suspendisse fermentum erat rhoncus metus vulputate, a aliquet ligula luctus.</p>
    <p>Sed est turpis, bibendum id nunc sit amet, tristique tempus risus. Integer in lorem mollis, tempor leo nec, fermentum nisl. Sed interdum viverra congue. Sed accumsan elit tempor lacus blandit, non gravida massa rutrum. Nam id pharetra mauris.</p>
  </div>
  <div class="article-photo second" role="img" aria-label="Business people signing documents at a table"></div>
  <div class="article-body">
    <p>Lorem ipsum dolor sit amet, consectetur adipiscing elit. Sed id nibh leo. Vivamus tempor imperdiet auctor. Donec justo orci, scelerisque tincidunt turpis vel, pellentesque commodo ligula.</p>
    <p>Curabitur vehicula pharetra felis id pellentesque. Quisque tristique nisi volutpat, eleifend felis porttitor, mattis arcu. Suspendisse fermentum erat rhoncus metus vulputate, a aliquet ligula luctus.</p>
    <p>Sed est turpis, bibendum id nunc sit amet, tristique tempus risus. Integer in lorem mollis, tempor leo nec, fermentum nisl. Sed interdum viverra congue. Sed accumsan elit tempor lacus blandit, non gravida massa rutrum. Nam id pharetra mauris.</p>
  </div>
</article>

<h2 class="section-heading author-heading abs">Posted by</h2>
<div class="author-photo abs" role="img" aria-label="Portrait of the author"></div>
<div class="author-info abs">
  <p class="author-name">Tobias Wrenholt</p>
  <p class="author-role">Alpine Civic Appeals Chamber, Judge</p>
  <p class="small-text">Lorem ipsum dolor sit amet, consectetur adipiscing elit. Fusce ullamcorper turpis lectus, sed convallis mi porttitor eget. Duis ex risus, blandit at dui a, hendrerit tempus justo. Etiam maximus in elit non porttitor. Vestibulum venenatis at tellus vel blandit. Nulla non turpis posuere, feugiat quam rutrum, tincidunt tortor.</p>
  <div class="social-row"><span></span><span></span><span></span><span></span><span></span><span></span></div>
</div>

<h2 class="section-heading comments-heading abs">Comments</h2>

<div class="avatar avatar-one abs" role="img" aria-label="Portrait of the commenter"></div>
<div class="comment comment-one abs">
  <div class="comment-head"><span class="comment-name">Nora Vale</span><span class="comment-date">June 21, 2016 at 8:15pm</span></div>
  <p class="small-text">Lorem ipsum dolor sit amet, consectetur adipiscing elit. Fusce ullamcorper turpis lectus, sed convallis mi porttitor eget. Duis ex risus, blandit at dui a, hendrerit tempus justo. Etiam maximus in elit non porttitor. Vestibulum venenatis at tellus vel blandit. Nulla non turpis posuere, feugiat quam rutrum, tincidunt tortor. Nulla non turpis posuere, feugiat quam rutrum, tincidunt tortor.</p>
  <p class="reply"><svg width="10" height="9" viewBox="0 0 10 9"><path d="M4 1L1 4l3 3M1 4h5a3 3 0 0 1 3 3v1" stroke="#0455a3" stroke-width="1.4" fill="none"/></svg>Reply</p>
</div>

<div class="avatar avatar-two abs" role="img" aria-label="Portrait of the author replying"></div>
<div class="comment comment-two abs">
  <div class="comment-head"><span class="comment-name">Tobias Wrenholt</span><span class="comment-date">June 21, 2016 at 8:15pm</span></div>
  <p class="small-text">Lorem ipsum dolor sit amet, consectetur adipiscing elit. Fusce ullamcorper turpis lectus, sed convallis mi porttitor eget. Duis ex risus, blandit at dui a, hendrerit tempus justo. Etiam maximus in elit non porttitor. Vestibulum venenatis at tellus vel blandit. Nulla non turpis posuere, feugiat quam rutrum, tincidunt tortor.</p>
  <p class="reply"><svg width="10" height="9" viewBox="0 0 10 9"><path d="M4 1L1 4l3 3M1 4h5a3 3 0 0 1 3 3v1" stroke="#0455a3" stroke-width="1.4" fill="none"/></svg>Reply</p>
</div>

<div class="login-row abs">
  <span class="login-label">Login to comment</span>
  <button class="login-button" type="button">Login</button>
</div>

<footer>
  <div class="footer-band abs"></div>
  <div class="brand footer-brand abs">Tobias Wrenholt<span class="brand-sub">Notes from the Dais</span></div>
  <p class="copyright abs">© 2017 Tobias Wrenholt All rights reserved</p>
</footer>

</body>
</html>
```